4 x Designs Required

Hi There,
I require 4 x different designs to be made for 4 new brands of mine however they can be quite interchangeable. HR Plinkr and Marketing Plinkr can be similar just with a difference in colour. The same goes for the Bulletin brands. This means there are ultimately two designs that need perfecting.

There must be a click here CTA on the banner somewhere. :-)

I require the banners in 728x90 format and 960x90 please.

Please use strap lines on the banners such as:
Essential Whitepapers for HR Professionals
Essential Whitepapers for Marketing Professionals
Your No.1 Whitepaper Resource

The brand names:
HR Plinkr
Marketing Plinkr
HR Dispatchly
Marketing Dispatchly

Examples attached.

```html
<!DOCTYPE html>
<html lang="en">
<head>
<meta charset="utf-8">
<title>HR Plinkr &amp; HR Dispatchly Banners</title>
<link href="https://fonts.googleapis.com/css2?family=Poppins:wght@500;600&display=swap" rel="stylesheet">
<style>
  :root {
    --stage-light: #dcdcdc;
    --stage-dark: #b9b9b9;
    --plinkr-panel: #04141d;
    --plinkr-deep: #062b44;
    --plinkr-mid: #0a4a6a;
    --plinkr-accent: #00cde4;
    --dispatch-panel: #03300c;
    --dispatch-deep: #0b6a0b;
    --dispatch-mid: #2b9612;
    --dispatch-accent: #ffee00;
    --dispatch-stripe: #8fc31a;
    --cta-ink: #04141d;
    --white: #ffffff;
  }
  html, body {
    margin: 0;
    width: 1200px;
    height: 776px;
    overflow: hidden;
  }
  body {
    position: relative;
    background: radial-gradient(ellipse at 50% 45%, var(--stage-light) 0%, #d2d2d2 55%, var(--stage-dark) 100%);
    font-family: "Poppins", sans-serif;
  }
  .banner {
    position: absolute;
    left: 248px;
    height: 66px;
    overflow: hidden;
  }
  .banner--wide { width: 706px; }
  .banner--narrow { width: 535px; }

  .banner--plinkr {
    background: linear-gradient(100deg, var(--plinkr-mid) 0%, var(--plinkr-deep) 45%, var(--plinkr-mid) 75%, var(--plinkr-deep) 100%);
  }
  .banner--dispatch {
    background: linear-gradient(100deg, var(--dispatch-mid) 0%, var(--dispatch-deep) 50%, var(--dispatch-mid) 80%, var(--dispatch-deep) 100%);
  }

  .brand-stripe, .brand-panel {
    position: absolute;
    top: 0;
    height: 100%;
    clip-path: polygon(0 0, calc(100% - 24px) 0, 100% 50%, calc(100% - 24px) 100%, 0 100%);
  }
  .banner--plinkr .brand-panel { width: 170px; background: var(--plinkr-panel); }
  .banner--plinkr .brand-stripe {
    width: 177px;
    background: linear-gradient(180deg, rgba(0,205,228,0.25) 0%, var(--plinkr-accent) 100%);
  }
  .banner--dispatch .brand-panel { width: 190px; background: var(--dispatch-panel); }
  .banner--dispatch .brand-stripe {
    width: 197px;
    background: linear-gradient(180deg, rgba(143,195,26,0.3) 0%, var(--dispatch-stripe) 100%);
  }

  .brand-name {
    position: absolute;
    top: 0;
    height: 66px;
    line-height: 66px;
    margin: 0;
    font-weight: 600;
    white-space: nowrap;
    letter-spacing: -0.5px;
  }
  .banner--plinkr .brand-name { left: 20px; font-size: 31px; color: var(--plinkr-accent); }
  .banner--dispatch .brand-name { left: 10px; font-size: 25px; color: var(--dispatch-accent); }

  .tagline {
    position: absolute;
    top: 50%;
    transform: translateY(-50%);
    margin: 0;
    color: var(--white);
    font-weight: 500;
    white-space: nowrap;
  }
  .banner--plinkr .tagline { left: 200px; font-size: 18px; }
  .banner--dispatch .tagline { left: 222px; font-size: 16.5px; }
  .banner--narrow .tagline { line-height: 1.2; }
  .banner--plinkr.banner--narrow .tagline { font-size: 19px; line-height: 1.18; }
  .banner--dispatch.banner--narrow .tagline { font-size: 17.5px; line-height: 1.2; }

  .cta {
    position: absolute;
    right: 10px;
    top: 20px;
    width: 82px;
    height: 26px;
    border-radius: 6px;
    display: flex;
    align-items: center;
    justify-content: center;
    font-size: 9.5px;
    font-weight: 600;
    color: var(--cta-ink);
    text-decoration: none;
  }
  .banner--plinkr .cta { background: var(--plinkr-accent); }
  .banner--dispatch .cta { background: var(--dispatch-accent); }
</style>
</head>
<body>

  <section class="banner banner--plinkr banner--wide" style="top:164px">
    <div class="brand-stripe"></div>
    <div class="brand-panel"></div>
    <h2 class="brand-name">HR Plinkr</h2>
    <p class="tagline">Essential Whitepapers for HR Professionals</p>
    <a class="cta" href="#">CLICK HERE</a>
  </section>

  <section class="banner banner--plinkr banner--narrow" style="top:269px">
    <div class="brand-stripe"></div>
    <div class="brand-panel"></div>
    <h2 class="brand-name">HR Plinkr</h2>
    <p class="tagline">Essential Whitepapers<br>for HR Professionals</p>
    <a class="cta" href="#">CLICK HERE</a>
  </section>

  <section class="banner banner--dispatch banner--wide" style="top:425px">
    <div class="brand-stripe"></div>
    <div class="brand-panel"></div>
    <h2 class="brand-name">HR Dispatchly</h2>
    <p class="tagline">Essential Whitepapers for HR Professionals</p>
    <a class="cta" href="#">CLICK HERE</a>
  </section>

  <section class="banner banner--dispatch banner--narrow" style="top:526px">
    <div class="brand-stripe"></div>
    <div class="brand-panel"></div>
    <h2 class="brand-name">HR Dispatchly</h2>
    <p class="tagline">Essential Whitepapers<br>for HR Professionals</p>
    <a class="cta" href="#">CLICK HERE</a>
  </section>

</body>
</html>
```